Sign Design for Truck Repair Shop center

Need a road-side sign for a pickup truck repair shop called HaulPoint Garage. The logo is attached and should be used on the sign. The background should be white and the main part of the logo should take up a large part of the sign so it can be easily read by passing traffic. The sign is 4 feet tall by 8 feet wide. Also need to add the website address" "www.HaulPointGarage-example.com" and "Call/Text 555.382.4607"

```html
<!DOCTYPE html>
<html lang="en">
<head>
<meta charset="utf-8">
<title>HaulPoint Garage – Roadside Sign</title>
<link rel="stylesheet" href="https://fonts.googleapis.com/css2?family=Oswald:wght@500;600;700&display=swap">
<style>
  :root {
    --backdrop: #c8c8c8;
    --sign-white: #ffffff;
    --brand-blue: #0b55a3;
    --deep-blue: #0d2f66;
    --sky-blue: #8cc3f2;
    --steel-grey: #6d7479;
    --light-grey: #9aa1a6;
  }
  * { margin: 0; padding: 0; box-sizing: border-box; }
  html, body {
    width: 1091px; height: 1200px; overflow: hidden;
    background: var(--backdrop);
    font-family: "Oswald", "Arial Narrow", sans-serif;
  }
  .sign {
    position: absolute; left: 114px; top: 384px;
    width: 863px; height: 431px;
    background: var(--sign-white);
    box-shadow: -10px 10px 14px rgba(0,0,0,0.28);
    overflow: hidden;
  }
  .sign__shapes { position: absolute; inset: 0; }
  .brand-name {
    position: absolute; left: 40px; top: 34px; width: 430px;
    color: var(--brand-blue); font-weight: 700;
    font-size: 78px; line-height: 0.98; text-transform: uppercase;
    text-align: center; letter-spacing: 1px;
  }
  .contact-line {
    position: absolute; left: 40px; top: 252px;
    display: flex; align-items: center; gap: 12px;
  }
  .contact-line__label {
    color: var(--deep-blue); font-weight: 600; font-size: 25px;
    line-height: 1.05; padding-right: 10px;
    border-right: 2px solid var(--deep-blue);
  }
  .contact-line__number {
    color: var(--deep-blue); font-weight: 700; font-size: 68px;
    line-height: 1; letter-spacing: 1px;
    text-shadow: 3px 3px 0 var(--sky-blue);
  }
  .contact-rule {
    position: absolute; left: 130px; top: 341px; width: 373px; height: 2px;
    background: var(--brand-blue);
  }
  .website {
    position: absolute; left: 44px; top: 362px;
    display: flex; align-items: center; gap: 14px;
  }
  .website__icon { width: 36px; height: 36px; }
  .website__url {
    color: var(--brand-blue); font-weight: 600; font-size: 27px;
    text-transform: uppercase; text-shadow: 1px 1px 0 var(--sky-blue);
  }
  .service-title {
    position: absolute; right: 28px; top: 48px;
    color: var(--sign-white); font-weight: 700; font-size: 76px;
    line-height: 1.13; text-align: right; text-transform: uppercase;
    text-shadow: 3px 3px 0 var(--deep-blue);
  }
</style>
</head>
<body>
  <main class="sign">
    <svg class="sign__shapes" viewBox="0 0 863 431" width="863" height="431" aria-hidden="true">
      <path class="sign__accent-line" d="M 402 10 C 490 24 548 120 535 230" fill="none" stroke="var(--steel-grey)" stroke-width="7" stroke-linecap="round"/>
      <path class="sign__grey-band" d="M 420 0 H 545 C 628 115 625 240 592 312 L 656 431 H 630 L 555 318 C 592 245 585 95 420 0 Z" fill="var(--light-grey)"/>
      <path class="sign__blue-panel" d="M 535 0 H 863 V 431 H 656 L 592 312 C 625 240 628 115 535 0 Z" fill="var(--brand-blue)"/>
    </svg>

    <h1 class="brand-name">HaulPoint<br>Garage</h1>

    <div class="contact-line">
      <span class="contact-line__label">CALL<br>TEXT</span>
      <span class="contact-line__number">555.382.4607</span>
    </div>
    <div class="contact-rule"></div>

    <div class="website">
      <svg class="website__icon" viewBox="0 0 36 36" aria-hidden="true">
        <circle cx="18" cy="18" r="17" fill="var(--brand-blue)"/>
        <g fill="none" stroke="#fff" stroke-width="1.6">
          <ellipse cx="18" cy="18" rx="7" ry="17"/>
          <line x1="18" y1="1" x2="18" y2="35"/>
          <line x1="1" y1="18" x2="35" y2="18"/>
          <line x1="4" y1="10" x2="32" y2="10"/>
          <line x1="4" y1="26" x2="32" y2="26"/>
        </g>
      </svg>
      <span class="website__url">www.HaulPointGarage-example.com</span>
    </div>

    <h2 class="service-title">Truck<br>Repair<br>Shop</h2>
  </main>
</body>
</html>
```